Nur Briefpapier und VK für Pflegedienst, Logo vorhanden!!!!
Zielgruppe
Wir sind ein Pflegedienst, unsere Zielgruppe sind Krankenkassen und Patienten und andere Krankenhäuser mit denen wir zusammen arbeiten.
Aufgabenstellung
modern, seriös, elitär

```html
<!DOCTYPE html>
<html lang="de">
<head>
<meta charset="UTF-8">
<title>Fenrokare Pflegedienste – Visitenkarte</title>
<link rel="stylesheet" href="https://fonts.googleapis.com/css2?family=Fira+Sans:wght@400;500&display=swap">
<style>
  :root {
    --brand-red: #e11f2b;
    --paper: #ffffff;
    --edge: #9a9a9a;
  }
  * { margin: 0; padding: 0; box-sizing: border-box; }
  html, body {
    width: 1200px;
    height: 804px;
    overflow: hidden;
    background: var(--paper);
  }
  .business-card {
    position: relative;
    width: 1200px;
    height: 804px;
    background: var(--paper);
    border: 1px solid var(--edge);
    font-family: "Fira Sans", sans-serif;
    overflow: hidden;
  }
  .brand-area {
    position: absolute;
    left: 0;
    top: 0;
    width: 579px;
    height: 100%;
    display: flex;
    flex-direction: column;
    align-items: center;
    justify-content: center;
    gap: 34px;
  }
  .brand-dot {
    width: 96px;
    height: 96px;
    border-radius: 50%;
    background: var(--brand-red);
  }
  .brand-name {
    color: var(--brand-red);
    font-weight: 500;
    font-size: 64px;
    line-height: 1.15;
    text-align: center;
  }
  .brand-name span { display: block; font-size: 52px; }
  .info-panel {
    position: absolute;
    left: 579px;
    top: 0;
    right: 0;
    bottom: 0;
    background: var(--brand-red);
  }
  .service-band {
    position: absolute;
    left: 0;
    right: 0;
    top: 119px;
    height: 188px;
    background: var(--paper);
    padding: 34px 0 0 35px;
  }
  .service-title {
    color: var(--brand-red);
    font-weight: 400;
    font-size: 46px;
    line-height: 68px;
  }
  .contact {
    position: absolute;
    left: 35px;
    top: 386px;
    color: var(--paper);
  }
  .contact-name {
    font-weight: 400;
    font-size: 48px;
    line-height: 58px;
  }
  .contact-role {
    font-size: 34px;
    line-height: 48px;
    margin-bottom: 46px;
  }
  .contact-address {
    font-style: normal;
    font-size: 43px;
    line-height: 60px;
  }
</style>
</head>
<body>
  <div class="business-card">
    <div class="brand-area">
      <div class="brand-dot"></div>
      <div class="brand-name">Fenrokare<span>Pflegedienste</span></div>
    </div>
    <div class="info-panel">
      <div class="service-band">
        <h1 class="service-title">Häusliche Alten-<br>und Krankenpflege</h1>
      </div>
      <div class="contact">
        <p class="contact-name">Jonas Beispielmann</p>
        <p class="contact-role">Pflegefachkraft</p>
        <address class="contact-address">
          Birkenweg 27<br>
          45127 Musterstadt<br>
          Tel. 0201 - 55 01 234
        </address>
      </div>
    </div>
  </div>
</body>
</html>
```